Tovrelan Ltda

Logo design focused on: - Construction of civil works - Electrical services - Metal structures - Equipment rental Tomás Ibarra Leiva Manager tovrelan.ltda@brevomail.example 56 9 48215037 Quelitoco s / n, Sorimar, Valle de Quilmar

Building

Colors
33a6d7
0292cd
33b8a4
0555a3

```html
<!DOCTYPE html>
<html lang="es">
<head>
<meta charset="utf-8">
<title>Tovrelan Ltda – Tarjetas de presentación</title>
<link rel="stylesheet" href="https://fonts.googleapis.com/css2?family=Source+Sans+3:ital,wght@0,400;0,600;1,400&display=swap">
<style>
  :root {
    --backdrop: #2b2b2d;
    --card: #262c37;
    --card-edge: #1f242d;
    --sky: #33a6d7;
    --azure: #0292cd;
    --teal: #33b8a4;
    --navy: #0555a3;
    --text-soft: #aab2bd;
    --text-muted: #8a929d;
  }
  * { box-sizing: border-box; margin: 0; padding: 0; }
  html, body { width: 1200px; height: 716px; overflow: hidden; }
  body {
    background: var(--backdrop);
    font-family: "Source Sans 3", "Myriad Pro", sans-serif;
    position: relative;
  }
  .card {
    position: absolute;
    top: 203px;
    width: 540px;
    height: 310px;
    background: linear-gradient(160deg, #2b323e 0%, var(--card) 55%, var(--card-edge) 100%);
    border-radius: 4px;
    box-shadow: 0 10px 24px rgba(0,0,0,.45);
  }
  .card--back { left: 40px; }
  .card--front { left: 620px; }

  .brand { display: flex; align-items: center; gap: 14px; }
  .brand__dot {
    width: 46px; height: 46px; border-radius: 50%;
    background: var(--azure);
    flex: none;
  }
  .brand__name {
    font-size: 30px;
    font-weight: 400;
    color: var(--sky);
    letter-spacing: .5px;
  }

  .services {
    position: absolute; left: 42px; top: 46px;
    list-style: none;
    color: var(--text-soft);
    font-style: italic;
    font-size: 15px;
    line-height: 24px;
  }
  .services li::before {
    content: ""; display: inline-block;
    width: 6px; height: 6px; border-radius: 50%;
    background: var(--azure);
    margin-right: 6px; vertical-align: middle;
  }
  .card--back .brand { position: absolute; left: 230px; top: 180px; }

  .card--front .brand { position: absolute; left: 34px; top: 108px; }
  .divider {
    position: absolute; left: 296px; top: 48px;
    width: 2px; height: 214px;
    background: var(--navy);
  }
  .contact { position: absolute; left: 322px; top: 74px; }
  .contact__name { font-size: 22px; color: var(--text-soft); line-height: 1.1; }
  .contact__role { font-size: 15px; color: var(--azure); margin-bottom: 18px; }
  .contact__row {
    display: flex; align-items: flex-start; gap: 8px;
    font-size: 13.5px; color: var(--text-muted); line-height: 1.3;
    margin-bottom: 8px;
  }
  .contact__row svg { flex: none; margin-top: 2px; }
</style>
</head>
<body>

<section class="card card--back" aria-label="Reverso de la tarjeta">
  <ul class="services">
    <li>Construcción de Obras Civiles</li>
    <li>Servicios eléctricos</li>
    <li>Estructuras metálicas</li>
    <li>Arriendo de Equipos</li>
  </ul>
  <div class="brand">
    <span class="brand__dot"></span>
    <span class="brand__name">Tovrelan Ltda</span>
  </div>
</section>

<section class="card card--front" aria-label="Anverso de la tarjeta">
  <div class="brand">
    <span class="brand__dot"></span>
    <span class="brand__name">Tovrelan Ltda</span>
  </div>
  <div class="divider"></div>
  <div class="contact">
    <p class="contact__name">Tomás Ibarra Leiva</p>
    <p class="contact__role">Gerente</p>
    <p class="contact__row">
      <svg width="14" height="11" viewBox="0 0 14 11" aria-hidden="true"><rect x="0.5" y="0.5" width="13" height="10" rx="1" fill="var(--teal)"/><path d="M1 1.5 7 6l6-4.5" stroke="#262c37" stroke-width="1.3" fill="none"/></svg>
      tovrelan.ltda@brevomail.example
    </p>
    <p class="contact__row">
      <svg width="14" height="12" viewBox="0 0 14 12" aria-hidden="true"><path d="M1 4c0-2 3-3 6-3s6 1 6 3v1h-3V3.5H4V5H1z" fill="var(--teal)"/><rect x="3" y="6" width="8" height="5.5" rx="1" fill="var(--teal)"/></svg>
      +56 9 48215037
    </p>
    <p class="contact__row">
      <svg width="12" height="15" viewBox="0 0 12 15" aria-hidden="true"><path d="M6 0a5 5 0 0 0-5 5c0 3.8 5 10 5 10s5-6.2 5-10a5 5 0 0 0-5-5z" fill="var(--teal)"/><circle cx="6" cy="5" r="1.8" fill="#262c37"/></svg>
      <span>Quelitoco s/n, Sorimar<br>Valle de Quilmar</span>
    </p>
  </div>
</section>

</body>
</html>
```